Veltrove Limited Business Card Design Project

Veltrove Limited is my UK based company used as my brand to work as an Interim Manager or contractor in project/programme management and Non-Executive Director.

Veltrove is Latin for 'execute' as in getting things done rather than killing people!

Logo and design needs to promote reliable, professional, and successful project delivery. Simple, elegant, clean, professional are words that should spring to mind!

Target Market(s)

Middle and senior management in english speaking countries aged 35 - 60 that hire and task qualified and experienced project/programme managers and Non-Executive Directors.

Industry/Entity Type

Contractor

Font styles to use
Serif
Sans Serif

Requirements
Must have
• Mobile telephone number 07846 215098
email address marcushale@veltrove.co.uk
Nice to have
• LinkedIn link to my profile.

Interim Manager
Should not have
• avoid Ticks and clocks

```html
<!DOCTYPE html>
<html lang="en">
<head>
<meta charset="utf-8">
<title>Veltrove Limited – Business Card Options</title>
<link rel="stylesheet" href="https://fonts.googleapis.com/css2?family=Exo+2:wght@400;500&display=swap">
<style>
  :root {
    --ink: #353a3b;
    --teal: #135e6a;
    --cyan: #1fb3c9;
    --paper: #ffffff;
    --board: #e6e7e9;
    --label: #b9bcbf;
    --edge: #d2d4d6;
  }
  * { box-sizing: border-box; margin: 0; padding: 0; }
  html, body { width: 960px; height: 1200px; overflow: hidden; }
  body { position: relative; background: var(--board); font-family: "Exo 2", sans-serif; color: var(--ink); }

  .sheet-top { position: absolute; left: 0; top: 0; width: 960px; height: 720px; background: var(--paper); }
  .sheet-shadow { position: absolute; left: 0; top: 720px; width: 960px; height: 36px;
    background: radial-gradient(ellipse 60% 100% at 50% 0, rgba(0,0,0,.55), rgba(0,0,0,0) 70%); }

  .card { position: absolute; width: 321px; height: 184px; overflow: hidden; background: var(--paper); border: 1px solid var(--edge); }
  .card.dark { background: var(--ink); border-color: var(--ink); }
  .col-left { left: 146px; } .col-right { left: 492px; }

  .option-label { position: absolute; font-size: 14px; letter-spacing: .5px; color: var(--label); font-weight: 400; }

  .brand { position: absolute; display: flex; align-items: center; gap: 9px; font-weight: 500; letter-spacing: 2px; color: var(--ink); }
  .dark .brand { color: var(--paper); }
  .brand .mark { width: 14px; height: 14px; background: var(--cyan); flex: none; }
  .brand-centre { left: 0; right: 0; top: 0; bottom: 0; justify-content: center; font-size: 23px; }

  .brand-block { position: absolute; display: flex; flex-direction: column; align-items: center; gap: 8px; font-weight: 500; letter-spacing: 1.5px; color: var(--ink); }
  .brand-block .mark { background: var(--teal); }

  .person { position: absolute; line-height: 1; }
  .person .name { font-size: 14px; letter-spacing: .6px; font-weight: 400; }
  .person .role { font-size: 8.5px; color: var(--cyan); margin-top: 2px; letter-spacing: .3px; }
  .dark .person .name { color: var(--paper); }

  .contacts { position: absolute; list-style: none; font-size: 11px; line-height: 17.5px; font-weight: 500; letter-spacing: .2px; }
  .contacts li { display: flex; align-items: center; gap: 6px; }
  .contacts svg { width: 10px; height: 10px; flex: none; }
  .dark .contacts, .panel .contacts { color: var(--paper); }

  .panel { position: absolute; top: 62px; height: 60px; background: var(--ink); }
  .panel.teal { background: var(--teal); }
  .panel .person { left: 12px; top: 20px; }
  .panel.teal .person .name { color: var(--paper); }
  .panel.teal .person .role { color: var(--paper); }
  .panel .person .name { color: var(--paper); }

  .stripe { position: absolute; left: 0; width: 100%; background: var(--teal); }
  .stripe.wide { top: 142px; height: 19px; }
  .stripe.thin { top: 165px; height: 3px; background: #1a8796; }
</style>
</head>
<body>
<svg width="0" height="0" style="position:absolute" aria-hidden="true">
  <defs>
    <symbol id="i-phone" viewBox="0 0 10 10"><circle cx="5" cy="5" r="5" fill="#1fb3c9"/><path d="M3.2 2.4l1 1.2-.5.6c.4.8 1 1.4 1.8 1.8l.6-.5 1.2 1-.6.9C4.9 7.4 2.6 5.1 2.3 3z" fill="#fff"/></symbol>
    <symbol id="i-mail" viewBox="0 0 10 10"><rect x="0" y="2" width="10" height="6.5" fill="#1fb3c9"/><path d="M0.4 2.4L5 6l4.6-3.6M0.4 8.1l3.3-3M9.6 8.1l-3.3-3" stroke="#fff" stroke-width=".7" fill="none"/></symbol>
    <symbol id="i-web" viewBox="0 0 10 10"><circle cx="5" cy="5" r="5" fill="#1fb3c9"/><path d="M5 0v10M0 5h10M1.5 2.5h7M1.5 7.5h7" stroke="#fff" stroke-width=".6"/><ellipse cx="5" cy="5" rx="2.2" ry="5" stroke="#fff" stroke-width=".6" fill="none"/></symbol>
  </defs>
</svg>

<div class="sheet-top"></div>
<div class="sheet-shadow"></div>

<!-- Option 01 -->
<section class="card col-left" style="top:43px">
  <div class="brand brand-centre"><span class="mark"></span>VELTROVE</div>
</section>
<section class="card col-right dark" style="top:43px">
  <div class="person" style="left:50px;top:32px"><div class="name">Marcus Hale</div><div class="role">Interim Manager</div></div>
  <ul class="contacts" style="left:31px;top:104px">
    <li><svg><use href="#i-phone"/></svg>07846 215098</li>
    <li><svg><use href="#i-mail"/></svg>marcushale@veltrove.co.uk</li>
    <li><svg><use href="#i-web"/></svg>www.veltrove.co.uk</li>
  </ul>
  <div class="brand-block" style="left:228px;top:58px;font-size:12px;color:#fff"><span class="mark" style="width:44px;height:44px;background:var(--cyan)"></span>VELTROVE</div>
</section>
<div class="option-label" style="left:836px;top:212px">OPTION 01</div>

<!-- Option 02 -->
<section class="card col-left dark" style="top:250px">
  <div class="brand brand-centre"><span class="mark"></span>VELTROVE</div>
</section>
<section class="card col-right" style="top:250px">
  <div class="person" style="left:50px;top:32px"><div class="name">Marcus Hale</div><div class="role">Interim Manager</div></div>
  <ul class="contacts" style="left:31px;top:104px">
    <li><svg><use href="#i-phone"/></svg>07846 215098</li>
    <li><svg><use href="#i-mail"/></svg>marcushale@veltrove.co.uk</li>
    <li><svg><use href="#i-web"/></svg>www.veltrove.co.uk</li>
  </ul>
  <div class="brand-block" style="left:228px;top:58px;font-size:12px"><span class="mark" style="width:44px;height:44px"></span>VELTROVE</div>
</section>
<div class="option-label" style="left:836px;top:420px">OPTION 02</div>

<!-- Option 03 -->
<section class="card col-left" style="top:458px">
  <div class="brand" style="left:14px;top:80px;font-size:17px;letter-spacing:1.5px"><span class="mark" style="width:11px;height:11px"></span>VELTROVE</div>
  <div class="panel" style="left:187px;width:134px">
    <div class="person" style="top:17px"><div class="name">Marcus Hale</div><div class="role">Interim Manager</div></div>
  </div>
</section>
<section class="card col-right" style="top:458px">
  <div class="panel" style="left:0;width:201px">
    <ul class="contacts" style="left:25px;top:4px">
      <li><svg><use href="#i-phone"/></svg>07846 215098</li>
      <li><svg><use href="#i-mail"/></svg>marcushale@veltrove.co.uk</li>
      <li><svg><use href="#i-web"/></svg>www.veltrove.co.uk</li>
    </ul>
  </div>
  <div class="brand-block" style="left:226px;top:64px;font-size:11px"><span class="mark" style="width:32px;height:32px"></span>VELTROVE</div>
</section>
<div class="option-label" style="left:836px;top:623px">OPTION 03</div>

<!-- Option 04 -->
<section class="card col-left" style="top:759px">
  <div class="panel teal" style="left:0;width:134px">
    <div class="person" style="left:28px;top:18px"><div class="name">Marcus Hale</div><div class="role" style="font-size:8px">Interim Manager</div></div>
  </div>
  <div class="brand" style="left:150px;top:80px;font-size:17px;letter-spacing:1.5px"><span class="mark" style="width:11px;height:11px"></span>VELTROVE</div>
</section>
<section class="card col-right" style="top:759px">
  <div class="brand-block" style="left:26px;top:64px;font-size:11px"><span class="mark" style="width:34px;height:34px"></span>VELTROVE</div>
  <div class="panel teal" style="left:121px;width:200px">
    <ul class="contacts" style="left:10px;top:4px">
      <li><svg><use href="#i-phone"/></svg>07846 215098</li>
      <li><svg><use href="#i-mail"/></svg>marcushale@veltrove.co.uk</li>
      <li><svg><use href="#i-web"/></svg>www.veltrove.co.uk</li>
    </ul>
  </div>
</section>
<div class="option-label" style="left:822px;top:925px">OPTION 04</div>

<!-- Option 05 -->
<section class="card col-left dark" style="top:970px">
  <div class="brand" style="left:0;right:0;top:0;height:142px;justify-content:center;font-size:23px"><span class="mark"></span>VELTROVE</div>
  <div class="stripe wide"></div>
  <div class="stripe thin"></div>
</section>
<section class="card col-right" style="top:970px">
  <div class="person" style="left:50px;top:32px"><div class="name">Marcus Hale</div><div class="role">Interim Manager</div></div>
  <ul class="contacts" style="left:31px;top:80px">
    <li><svg><use href="#i-phone"/></svg>07846 215098</li>
    <li><svg><use href="#i-mail"/></svg>marcushale@veltrove.co.uk</li>
    <li><svg><use href="#i-web"/></svg>www.veltrove.co.uk</li>
  </ul>
  <div class="brand-block" style="left:228px;top:44px;font-size:12px"><span class="mark" style="width:44px;height:44px"></span>VELTROVE</div>
  <div class="stripe wide"></div>
  <div class="stripe thin"></div>
</section>
<div class="option-label" style="left:822px;top:1139px">OPTION 05</div>
</body>
</html>
```